Life insurance company website and landing page

Web design is required for life insurance company. Specifically the company will 1) generate leads and 2) provide a blog. The target market of this business is people in their 50s and 60s, medium-high to high income earners, who are likely to have a policy in place already but want to save money on their premiums. Please read the attached design brief for more guidance. Open to any concepts that might work.The outputs for this job will include:1) a website2) a landing page3) fixing logos into a more useful and professional format (this should take 5 mins with the correct software)
Colors
Designer to choose colors to be used in the design.
Look and feel
Each slider illustrates characteristics of the customer's brand and the style your logo design should communicate.

```html
<!DOCTYPE html>
<html lang="en">
<head>
<meta charset="utf-8">
<title>CoverWise.Life — Compare Life Insurers</title>
<link href="https://fonts.googleapis.com/css2?family=Lato:wght@400;700;900&display=swap" rel="stylesheet">
<style>
:root{
  --red:#e8252b;
  --red-dark:#c91c22;
  --ink:#1e1e1e;
  --muted:#777;
  --soft:#f1f1f1;
  --line:#e6e6e6;
  --footer:#1c1c1c;
  --white:#fff;
}
*{box-sizing:border-box;margin:0;padding:0}
html,body{width:1200px;height:4501px;overflow:hidden}
body{position:relative;font-family:'Lato',sans-serif;color:var(--ink);background:var(--white)}
.abs{position:absolute}
.btn{position:absolute;background:var(--red);color:#fff;font-weight:700;display:flex;align-items:center;justify-content:center;border-radius:3px;box-shadow:0 3px 6px rgba(200,30,30,.25)}
.btn.dark{background:#111;box-shadow:none}
.label{position:absolute;left:0;width:1200px;text-align:center;color:var(--red);font-size:18px}
.heading{position:absolute;left:0;width:1200px;text-align:center;font-size:36px;font-weight:400;color:var(--ink)}
.para{position:absolute;text-align:center;font-size:11.5px;line-height:19px;color:var(--muted)}
.art{position:absolute;border-radius:24px}
.card{position:absolute;background:#fff;border:1px solid var(--line);box-shadow:0 4px 14px rgba(0,0,0,.08);border-radius:3px}
.card h3{font-size:17px;font-weight:700;color:var(--ink)}
.card p{font-size:11px;line-height:19px;color:var(--muted)}

/* header */
.site-header{position:absolute;top:0;left:0;width:1200px;height:88px;border-bottom:1px solid var(--line)}
.brand{position:absolute;left:162px;top:22px;display:flex;align-items:center;gap:10px;font-size:29px;color:var(--ink)}
.brand-mark{width:40px;height:40px;border:3px solid var(--red);border-radius:8px}
.nav{position:absolute;top:0;height:88px;display:flex}
.nav a{font-size:12px;color:#555;text-decoration:none;display:flex;align-items:center;justify-content:center;width:82px;border-left:1px solid var(--line)}
.nav a.active{color:var(--red)}

/* hero */
.hero-title{position:absolute;left:162px;top:188px;font-size:49px;line-height:57px;font-weight:400}
.hero-title em{font-style:normal;color:var(--red)}
.hero-sub{position:absolute;left:162px;top:374px;font-size:13px;line-height:21px;color:var(--muted)}
.dots{position:absolute;top:587px;left:855px;display:flex;gap:24px}
.dots i{width:13px;height:13px;border-radius:50%;background:#d0d0d0;display:block}
.dots i.on{background:var(--red)}

/* services */
.svc-text{position:absolute;left:162px;color:#fff}

/* types */
.type{position:absolute;width:150px;text-align:center;font-size:13px;font-weight:700;line-height:19px}
.type .ring{width:70px;height:70px;border-radius:50%;margin:0 auto 12px;box-shadow:0 3px 10px rgba(0,0,0,.1);display:flex;align-items:center;justify-content:center;background:#fff}
.type .ring span{width:30px;height:30px;border-radius:50%;background:var(--red);opacity:.85}

/* partners */
.partners{position:absolute;top:2082px;left:0;width:1200px;height:338px;background:var(--soft)}
.partner{position:absolute;top:2269px;width:136px;height:90px;background:#fff;border:1px solid var(--line);display:flex;align-items:center;justify-content:center}
.partner span{width:70px;height:36px;border-radius:18px}

/* testimonials */
.avatar{position:absolute;width:76px;height:76px;border-radius:50%;border:3px solid #fff;box-shadow:0 2px 8px rgba(0,0,0,.15)}
.client{font-size:12px;color:var(--red);text-align:center}

/* blog */
.blog{position:absolute;top:3365px;left:0;width:1200px;height:449px;background:var(--soft)}
.post{position:absolute;top:3522px;width:276px;height:220px;background:#fff;padding:20px 12px}
.post h4{font-size:13px;font-weight:700}
.post .date{font-size:10px;color:var(--red);margin:6px 0 4px}
.post p{font-size:11px;line-height:19px;color:var(--muted)}

/* footer */
.footer{position:absolute;top:4163px;left:0;width:1200px;height:338px;background:var(--footer);color:#ddd}
.footer h5{position:absolute;top:60px;font-size:14px;color:var(--red);font-weight:400}
.footer .txt{position:absolute;font-size:11px;line-height:19px;color:#ddd}
.social{position:absolute;top:195px;left:162px;display:flex;gap:12px}
.social i{width:32px;height:32px;border-radius:50%;border:2px solid #ddd;display:block}
</style>
</head>
<body>

<header class="site-header">
  <div class="brand"><span class="brand-mark"></span>CoverWise.Life</div>
  <nav class="nav" style="left:558px">
    <a href="#">Home</a><a href="#" class="active">About Us</a><a href="#">Services</a><a href="#">Blog</a><a href="#" style="border-right:1px solid var(--line)">Contact Us</a>
  </nav>
  <svg class="abs" style="left:1016px;top:33px" width="24" height="24" viewBox="0 0 24 24" fill="none" stroke="#c91c22" stroke-width="2.6"><circle cx="10" cy="10" r="7"/><line x1="15" y1="15" x2="22" y2="22"/></svg>
</header>

<!-- hero -->
<section>
  <svg class="abs" style="left:0;top:91px" width="1200" height="547" viewBox="0 0 1200 547">
    <path d="M1000 0 L1200 0 L1200 547 L1120 500 C1140 420 1100 330 1160 250 C1200 200 1180 120 1120 100 C1060 70 1010 60 1000 0Z" fill="var(--red)"/>
  </svg>
  <div class="art" role="img" aria-label="Illustration of a family sitting together among plants and clouds" style="left:625px;top:130px;width:520px;height:430px;border-radius:50% 45% 40% 50%;background:linear-gradient(135deg,#cfe7f3,#f4b08a 55%,#4a66c4)"></div>
  <h1 class="hero-title">Compare Australia's<br>leading <em>life Insurers</em><br>free today</h1>
  <p class="hero-sub">Make sure your insurer isn't charging you too much.<br>We only work with Australia's most trusted brands</p>
  <div class="btn" style="left:162px;top:440px;width:217px;height:51px;font-size:16px">Compare Quotes Now</div>
  <div class="dots"><i></i><i class="on"></i><i></i><i></i></div>
</section>

<!-- about -->
<div class="label" style="top:715px">About Us</div>
<h2 class="heading" style="top:742px">Insurance Made Simple For You</h2>
<p class="para" style="left:335px;top:794px;width:530px">Lorem Ipsum is simply dummy text of the printing and typesetting industry. Lorem Ipsum has been the industry's standard dummy text ever since the 1500s, when an unknown printer took a galley of type and scrambled it to make a type specimen book. It has survived not only five centuries, but also the leap into electronic typesetting, remaining essentially unchanged.</p>
<div class="btn" style="left:545px;top:915px;width:110px;height:37px;font-size:14px">Read More</div>

<!-- services -->
<svg class="abs" style="left:0;top:943px" width="560" height="385" viewBox="0 0 560 385">
  <path d="M0 20 C60 0 160 -10 220 10 C270 30 260 120 300 170 C340 210 470 150 530 220 C560 270 540 340 480 385 L0 385Z" fill="var(--red)"/>
</svg>
<div class="svc-text" style="top:1081px;font-size:18px">Our Services</div>
<div class="svc-text" style="top:1113px;font-size:35px;font-weight:700;line-height:45px">Insurance Made<br>Simple For You</div>
<div class="btn dark" style="left:162px;top:1228px;width:125px;height:37px;font-size:14px">Call To Action</div>

<div class="card" style="left:531px;top:1025px;width:232px;height:268px;padding:30px 17px">
  <h3>Life Insurance</h3>
  <p style="margin-top:6px">The insurance information source, will basically be the blog section of the website</p>
  <div role="img" aria-label="Illustration of a family beside a life insurance document" style="margin:14px auto 0;width:140px;height:110px;border-radius:10px;background:linear-gradient(135deg,#f3e6d2,#7f9fd6)"></div>
</div>
<div class="card" style="left:800px;top:1092px;width:232px;height:265px;padding:30px 17px">
  <h3>Insurance Brokering</h3>
  <p style="margin-top:6px">The insurance brokering service, is very important as this will directly generate revenue.</p>
  <div role="img" aria-label="Illustration of people with a shield and umbrella" style="margin:14px auto 0;width:150px;height:100px;border-radius:10px;background:linear-gradient(135deg,#5a6fc4,#f0d5c3)"></div>
</div>

<!-- other types -->
<div class="label" style="top:1415px">Life Insurance</div>
<h2 class="heading" style="top:1441px">Other types of Life Insurance</h2>
<div class="type" style="left:156px;top:1515px"><div class="ring" role="img" aria-label="TPD insurance icon"><span></span></div>TPD<br>Insurance</div>
<div class="type" style="left:304px;top:1515px"><div class="ring" role="img" aria-label="Income protection icon"><span></span></div>Income<br>Protection</div>
<div class="type" style="left:451px;top:1515px"><div class="ring" role="img" aria-label="Trauma insurance icon"><span></span></div>Trauma<br>Insurance</div>
<div class="type" style="left:598px;top:1515px"><div class="ring" role="img" aria-label="Family insurance icon"><span></span></div>Life insurance<br>for Families</div>
<div class="type" style="left:748px;top:1515px"><div class="ring" role="img" aria-label="Seniors insurance icon"><span></span></div>Seniors life<br>Insurance</div>
<div class="type" style="left:895px;top:1515px"><div class="ring" role="img" aria-label="Women insurance icon"><span></span></div>Life insurance<br>for Women</div>

<!-- what we do -->
<div class="abs" style="left:162px;top:1753px;color:var(--red);font-size:18px">Our Work</div>
<h2 class="abs" style="left:162px;top:1785px;font-size:36px;font-weight:400">What We Do</h2>
<p class="abs" style="left:162px;top:1848px;width:360px;font-size:11px;line-height:19px;color:var(--muted)">CoverWise.Life helps you find the most appropriate and cost effective options by comparing a variety of leading insurers at the same time</p>
<div class="btn" style="left:162px;top:1936px;width:168px;height:36px;font-size:14px">Get Free Quotes Now</div>
<div class="art" role="img" aria-label="Illustration of a family comparing options on a laptop at a shop counter" style="left:611px;top:1703px;width:481px;height:323px;border-radius:45% 50% 30% 40%;background:linear-gradient(135deg,#e4e6f2,#f7c6b6 50%,#3c4fa8)"></div>

<!-- partners -->
<section class="partners"></section>
<div class="label" style="top:2140px">Our Partner</div>
<h2 class="heading" style="top:2166px">Insurance Partner</h2>
<p class="para" style="left:0;width:1200px;top:2215px">Australia's leading insurers, we can help you compare them.</p>
<div class="partner" style="left:162px"><span style="background:#f2a51c"></span></div>
<div class="partner" style="left:310px"><span style="background:#2c8a3c"></span></div>
<div class="partner" style="left:458px"><span style="background:#1c4fa0"></span></div>
<div class="partner" style="left:606px"><span style="background:#f7c400"></span></div>
<div class="partner" style="left:755px"><span style="background:#2a74b8"></span></div>
<div class="partner" style="left:903px"><span style="background:#7ab826"></span></div>

<!-- key benefits -->
<svg class="abs" style="left:660px;top:2500px" width="540" height="385" viewBox="0 0 540 385">
  <path d="M540 0 L540 385 L140 385 C60 385 0 330 10 250 C20 170 120 170 190 140 C250 110 240 40 300 20 C360 0 460 30 540 0Z" fill="var(--red)"/>
</svg>
<div class="abs" style="left:664px;width:372px;text-align:right;top:2646px;font-size:18px;color:#fff">Key Benefits</div>
<div class="abs" style="left:664px;width:372px;text-align:right;top:2678px;font-size:32px;font-weight:700;line-height:38px;color:#fff">Insuarance Made<br>Simple For You</div>
<div class="btn dark" style="left:914px;top:2792px;width:126px;height:35px;font-size:14px">Call To Action</div>

<div class="card" style="left:161px;top:2479px;width:229px;height:225px;padding:30px 16px">
  <h3 style="font-size:15px">We only work with Aust...</h3>
  <p style="margin-top:4px;font-size:10.5px;letter-spacing:.3px">NEED A HIGH LEVEL OF COVER AT A LOW PRICE? - OUR HIGHLY EXPERIENCED BROKERS CAN..</p>
  <div role="img" aria-label="Illustration of a family with a shield" style="margin:12px auto 0;width:110px;height:75px;border-radius:10px;background:linear-gradient(135deg,#f0c6a8,#5a7fd1)"></div>
</div>
<div class="card" style="left:161px;top:2734px;width:229px;height:225px;padding:30px 16px">
  <h3 style="font-size:15px">No hidden fees</h3>
  <p style="margin-top:4px">No hidden fees - pay the same as going direct to the insurer, or even less</p>
  <div role="img" aria-label="Illustration of two people working at a laptop" style="margin:14px auto 0;width:120px;height:75px;border-radius:10px;background:linear-gradient(135deg,#2e4f8f,#e8373b)"></div>
</div>
<div class="card" style="left:416px;top:2615px;width:229px;height:224px;padding:30px 16px">
  <h3 style="font-size:15px">Price beat Guarantee</h3>
  <p style="margin-top:4px">Learn how life insurance works - For articles, videos, guides, and anything else life insurance.</p>
  <div role="img" aria-label="Illustration of a family holding a sign" style="margin:10px auto 0;width:90px;height:80px;border-radius:10px;background:linear-gradient(135deg,#f2c7a3,#3a5bb0)"></div>
</div>

<!-- testimonials -->
<div class="label" style="top:3003px">Testimonials</div>
<h2 class="heading" style="top:3028px">What Our Client Say</h2>
<div class="card" style="left:161px;top:3150px;width:430px;height:138px;padding:46px 24px 0">
  <div class="client">-Client Name</div>
  <p style="text-align:center;margin-top:4px">Lorem Ipsum is simply dummy text of the printing and typesetting industry. Lorem Ipsum has been the industry's standard dummy text ever since the 1500s.</p>
</div>
<div class="card" style="left:610px;top:3150px;width:431px;height:138px;padding:46px 24px 0">
  <div class="client">-Client Name</div>
  <p style="text-align:center;margin-top:4px">Lorem Ipsum is simply dummy text of the printing and typesetting industry. Lorem Ipsum has been the industry's standard dummy text ever since the 1500s.</p>
</div>
<div class="avatar" role="img" aria-label="Client portrait photo" style="left:336px;top:3112px;background:linear-gradient(135deg,#8a5a3c,#e0b59a)"></div>
<div class="avatar" role="img" aria-label="Client portrait photo" style="left:787px;top:3112px;background:linear-gradient(135deg,#d8d8d8,#2a2a2a)"></div>

<!-- blog -->
<section class="blog"></section>
<div class="label" style="top:3421px">Our Blog</div>
<h2 class="heading" style="top:3447px">Latest Insights</h2>
<article class="post" style="left:162px">
  <h4>Lorem Ipsum is simply dummy text of the</h4><div class="date">15 September 2019</div>
  <p>Lorem Ipsum is simply dummy text of the printing and typesetting industry. Lorem Ipsum has been the industry's standard dummy text ever since the 1500s.</p>
  <div class="btn" style="left:12px;top:172px;width:112px;height:36px;font-size:14px">Read More</div>
</article>
<article class="post" style="left:461px">
  <h4>Lorem Ipsum is simply dummy text of the</h4><div class="date">15 September 2019</div>
  <p>Lorem Ipsum is simply dummy text of the printing and typesetting industry. Lorem Ipsum has been the industry's standard dummy text ever since the 1500s.</p>
  <div class="btn" style="left:12px;top:172px;width:112px;height:36px;font-size:14px">Read More</div>
</article>
<article class="post" style="left:762px">
  <h4>Lorem Ipsum is simply dummy text of the</h4><div class="date">15 September 2019</div>
  <p>Lorem Ipsum is simply dummy text of the printing and typesetting industry. Lorem Ipsum has been the industry's standard dummy text ever since the 1500s.</p>
  <div class="btn" style="left:12px;top:172px;width:112px;height:36px;font-size:14px">Read More</div>
</article>

<!-- contact -->
<div class="label" style="top:3862px">Contact Us</div>
<h2 class="heading" style="top:3885px;font-size:29px;font-weight:700;line-height:44px">If you have any query then contact us now,<br>Don't hasitate</h2>
<p class="para" style="left:350px;top:3981px;width:500px">Lorem Ipsum is simply dummy text of the printing and typesetting industry. Lorem Ipsum has been the industry's standard dummy text ever since the 1500s.</p>
<div class="btn" style="left:484px;top:4057px;width:232px;height:48px;font-size:19px;font-weight:400;justify-content:flex-start;padding-left:12px;gap:14px">
  <svg width="34" height="34" viewBox="0 0 34 34"><rect width="34" height="34" rx="3" fill="#fff"/><path d="M11 9c2 0 3 4 2 5l-1 1c1 3 3 5 6 6l1-1c1-1 5 0 5 2l-1 3c-7 1-15-7-14-14z" fill="var(--red)"/></svg>
  +91-000-000-0000
</div>

<!-- footer -->
<footer class="footer">
  <div class="abs" style="left:162px;top:50px;display:flex;align-items:center;gap:8px;font-size:17px;color:#fff"><span style="width:26px;height:28px;border:2px solid var(--red);border-radius:5px"></span>CoverWise.Life</div>
  <div class="txt" style="left:162px;top:110px;width:215px;font-size:10px;line-height:19px">Lorem Ipsum is simply dummy text of the printing and typesetting industry. Lorem Ipsum has been the industry's.</div>
  <div class="social"><i></i><i></i><i></i><i></i></div>

  <h5 style="left:395px">Quick Link</h5>
  <div class="txt" style="left:395px;top:93px;line-height:20px"><span style="color:var(--red)">›</span> Terms of Use<br><span style="color:var(--red)">›</span> Privacy Policy<br><span style="color:var(--red)">›</span> Blog<br><span style="color:var(--red)">›</span> Contact Us</div>

  <h5 style="left:613px">Contact Info</h5>
  <svg class="abs" style="left:611px;top:96px" width="14" height="14" viewBox="0 0 14 14"><path d="M3 1c1 0 2 3 1 3L3 5c1 2 3 4 5 5l1-1c1-1 4 0 4 1l-1 3C7 13 1 7 1 2z" fill="var(--red)"/></svg>
  <div class="txt" style="left:642px;top:93px">+91-000-000-0000</div>
  <svg class="abs" style="left:611px;top:136px" width="14" height="11" viewBox="0 0 14 11"><rect width="14" height="11" fill="var(--red)"/><path d="M0 0l7 6 7-6" stroke="#1c1c1c" fill="none"/></svg>
  <div class="txt" style="left:642px;top:131px">info@coverwise.life</div>
  <svg class="abs" style="left:612px;top:170px" width="12" height="16" viewBox="0 0 12 16"><path d="M6 0a6 6 0 0 1 6 6c0 4-6 10-6 10S0 10 0 6a6 6 0 0 1 6-6z" fill="var(--red)"/><circle cx="6" cy="6" r="2.2" fill="#1c1c1c"/></svg>
  <div class="txt" style="left:642px;top:169px;width:160px">100- Lorem ipsum is simply dummy text.</div>

  <h5 style="left:837px">Newsletter</h5>
  <div class="txt" style="left:837px;top:93px;width:210px"><b style="color:#fff">SIGN UP FOR OUR NEWSLETTER -</b><br>Stay current with our news and insight</div>
  <div class="abs" style="left:837px;top:160px;width:202px;height:36px;background:#fff;font-size:10px;color:#888;padding:11px 12px">Enter Email</div>
  <div class="btn" style="left:837px;top:210px;width:110px;height:35px;font-size:12px">Subscribe Us</div>

  <div class="abs" style="left:162px;top:274px;width:878px;height:1px;background:#444"></div>
  <div class="abs" style="left:0;width:1200px;top:297px;text-align:center;font-size:11px;color:#ddd">© Copyright 2019 <span style="color:var(--red)">CoverWise Life</span>. Terms &amp; Conditions | Privacy Policy.</div>
</footer>

</body>
</html>
```